Webdesign für islamisches Bestattungsunternehmen
Zielgruppe
islamisches Bestattungsunternehmen, Grabsteine, Grabpflege
Aufgabenstellung
wir wollen ein elegantes design mit einem hauch an exklusivität. wir sind nicht auf billig aus, tatsächlich hochwertig, etwas teurer als die konkurrenz aber dafür bieten wir auch was an.
unser logo haben wir auch hier machen lassen.
www.nur-samira.eu
LEUTE!
Wir wünschen uns dass direkt auf der ersten seite die 3 optionen sofort ersichtlich sind!!! nicht dass die leute noch runterscrollen müssen...

```html
<!DOCTYPE html>
<html lang="de">
<head>
<meta charset="utf-8">
<title>Nur-Samira – Islamische Bestattungen</title>
<link href="https://fonts.googleapis.com/css2?family=Cinzel:wght@400;600;700&family=Poppins:wght@300;400;500&display=swap" rel="stylesheet">
<style>
:root{
  --gold:#c8951e;
  --gold-bar:#dfb655;
  --gold-form:#c4901f;
  --dark:#363434;
  --darker:#2b2a2a;
  --paper:#efece6;
  --ink:#2c2a28;
  --white:#ffffff;
  --parch-a:#e6c99a;
  --parch-b:#c99c5f;
}
*{box-sizing:border-box;margin:0;padding:0}
html,body{width:1200px;height:4408px;overflow:hidden}
body{position:relative;background:var(--paper);font-family:"Poppins",sans-serif;color:var(--ink)}
.abs{position:absolute}
.serif{font-family:"Cinzel",serif}
.photo{position:absolute}
.btn-outline{position:absolute;border:2px solid var(--gold);color:var(--gold);font-size:20px;display:flex;align-items:center;justify-content:center;background:transparent}
.btn-dark{border-color:var(--ink);color:var(--ink)}
.btn-light{border-color:#fff;color:#fff}
.social{display:flex;gap:8px}
.social span{width:34px;height:34px;border:2px solid var(--ink);border-radius:50%;display:block}
/* header */
.brand{left:104px;top:52px;font-family:"Cinzel",serif;font-weight:700;font-size:30px;color:var(--ink);display:flex;align-items:center;gap:12px}
.brand i{width:22px;height:22px;border:2px solid var(--ink);border-radius:50%;display:block}
.account{left:868px;top:22px;font-size:14px;color:#555;letter-spacing:.5px}
.phone{left:622px;top:84px;font-size:24px;color:var(--ink);display:flex;align-items:center;gap:18px}
.nav{left:0;top:146px;width:1200px;height:65px;background:var(--gold-bar)}
.nav ul{list-style:none;display:flex;position:absolute;left:113px;top:0;height:65px}
.nav li{font-family:"Cinzel",serif;font-size:15px;color:#3a2f1b;padding:0 18px;line-height:65px}
.nav li.active{background:var(--dark);color:#fff;font-weight:600;padding:0 14px}
.lang{left:930px;top:148px;width:95px;font-family:"Cinzel",serif;font-size:10px;text-align:center}
.lang div{height:22px;line-height:22px;background:#eee3c8;margin-bottom:2px}
/* hero */
.hero-panel{left:0;top:211px;width:513px;height:635px;background:var(--dark)}
.hero-title{left:115px;top:312px;font-size:46px;line-height:54px;color:var(--gold);font-weight:600}
.hero-rule{left:115px;top:440px;width:85px;height:6px;background:var(--gold)}
.hero-text{left:112px;top:488px;width:270px;font-size:13.5px;line-height:32px;color:#fff}
.hero-more{left:112px;top:690px;font-size:20px;color:var(--gold);font-weight:600}
.arrow{top:550px;width:36px;height:36px;border:2px solid #fff;border-radius:50%}
.thumb{top:605px;width:212px;height:241px;background:#fff}
.thumb .photo{left:0;top:0;width:212px;height:190px}
.thumb p{position:absolute;left:8px;top:202px;right:8px;font-size:8.5px;line-height:13px;color:#444}
/* services */
.sec-title{font-size:28px;line-height:36px;color:var(--gold);font-weight:600;text-align:center}
.sec-lead{left:270px;top:960px;width:660px;font-size:13.5px;line-height:22px;text-align:center;color:#333}
.book{left:113px;top:1020px;width:972px;height:585px;border:9px solid #1e1c1b;border-radius:14px;background:radial-gradient(ellipse at center,var(--parch-a),var(--parch-b))}
.svc{width:260px;text-align:center}
.svc .photo{position:relative;width:244px;height:155px;margin:0 auto;border:4px solid #fff}
.svc h3{font-family:"Cinzel",serif;font-size:27px;line-height:32px;color:#1f1c18;margin-top:16px;font-weight:600}
.svc p{font-size:13.5px;line-height:27px;margin-top:30px;color:#2c2620}
/* banner */
.banner{left:0;top:1633px;width:1200px;height:285px;background:linear-gradient(90deg,#3a3a38,#565553 50%,#3b3a38)}
.banner h2{position:absolute;left:0;top:70px;width:1200px;text-align:center;color:#fff;font-family:"Cinzel",serif;font-size:27px;line-height:37px;font-weight:600}
/* about */
.about-bg{left:0;top:1918px;width:1200px;height:457px;background:#fff}
.about-title{left:110px;top:1972px;font-size:28px;line-height:37px;color:var(--gold);font-weight:600}
.about-text{left:110px;top:2090px;width:360px;font-size:12.5px;line-height:26px;color:#333}
/* gallery */
.cell-text h4{font-family:"Cinzel",serif;font-size:22px;line-height:28px;color:var(--gold);font-weight:600}
.cell-text p{font-size:12.5px;line-height:21px;margin-top:10px;color:#333}
/* testimonial */
.quote{left:502px;top:3180px;width:560px;font-size:21px;line-height:42px;color:#444}
.dots{left:560px;top:3408px;display:flex;gap:6px}
.dots span{width:13px;height:13px;border-radius:50%;background:#333}
.dots span:first-child{background:var(--gold)}
/* contact */
.contact-card{left:102px;top:3636px;width:228px;height:265px;border:3px solid #2c2c2c;border-radius:8px;background:#fff;padding:36px 0 0 14px}
.contact-card div{display:flex;gap:14px;font-size:15.5px;line-height:19px;margin-bottom:28px;color:#333}
.contact-card svg{flex:none}
.form{left:625px;top:3560px;width:255px;height:475px;background:var(--gold-form);padding:30px 18px}
.form h3{color:#fff;font-family:"Cinzel",serif;font-size:27px;line-height:30px;text-align:center;font-weight:600}
.form .box{border:2px solid #fff;margin-top:22px;padding:12px 14px;height:330px}
.form label{display:block;color:#fff;font-size:8px;margin-top:10px}
.form .field{height:28px;background:#fff;margin-top:3px}
.form .send{margin-top:16px;height:30px;background:#2f2a22;color:#fff;font-size:9px;display:flex;align-items:center;justify-content:center}
/* footer */
.footer{left:0;top:4082px;width:1200px;height:326px;background:var(--darker);border-top:5px solid var(--gold)}
.footer h5{position:absolute;top:48px;font-family:"Cinzel",serif;font-size:15px;color:var(--gold);font-weight:600}
.footer ul{position:absolute;list-style:none;color:#fff;font-size:12px;line-height:26px}
.footer .social span{border-color:#fff}
</style>
</head>
<body>

<!-- header -->
<div class="abs brand"><i></i>NUR-SAMIRA</div>
<div class="abs account">SIGN UP &nbsp; | &nbsp; LOG IN</div>
<div class="abs phone">
  <svg width="24" height="24" viewBox="0 0 24 24"><path d="M6.6 10.8a15 15 0 006.6 6.6l2.2-2.2a1 1 0 011-.25 11 11 0 003.6.6 1 1 0 011 1V20a1 1 0 01-1 1A17 17 0 013 4a1 1 0 011-1h3.5a1 1 0 011 1 11 11 0 00.6 3.6 1 1 0 01-.25 1z" fill="#2c2a28"/></svg>
  0151-2030-4455
</div>
<div class="abs social" style="left:900px;top:79px"><span></span><span></span><span></span></div>

<nav class="abs nav">
  <ul><li class="active">HOME</li><li>FUNERAL</li><li>TOMBSTONES</li><li>MAINTENANCE</li><li>REVIEWS</li><li>CONTACT</li></ul>
</nav>
<div class="abs lang"><div>▾ ENGLISH</div><div>GERMAN</div></div>

<!-- hero -->
<div class="photo" role="img" aria-label="Mann vor einem Grabstein mit arabischer Inschrift" style="left:513px;top:211px;width:687px;height:635px;background:linear-gradient(135deg,#7a7b6a,#4a4c40 60%,#2f302b)"></div>
<div class="abs hero-panel"></div>
<h1 class="abs serif hero-title">EVERLASTING<br>PEACE</h1>
<div class="abs hero-rule"></div>
<p class="abs hero-text">Lorem Ipsum is simply dummy text of the printing and typesetting industry. Lorem Ipsum has been the industry's standard dummy text ever since the 1500s</p>
<div class="abs serif hero-more">READ MORE ››</div>
<svg class="abs arrow" style="left:417px" viewBox="0 0 36 36"><path d="M20 11l-7 7 7 7" stroke="#fff" stroke-width="2.5" fill="none"/></svg>
<svg class="abs arrow" style="left:465px" viewBox="0 0 36 36"><path d="M16 11l7 7-7 7" stroke="#fff" stroke-width="2.5" fill="none"/></svg>
<div class="abs thumb" style="left:418px"><div class="photo" role="img" aria-label="Mann neben Grabstein" style="background:linear-gradient(#6f7a5d,#3b3a33)"></div><p>Lorem ipsum is simply dummy text of the printing and typesetting industry. Lorem</p></div>
<div class="abs thumb" style="left:646px"><div class="photo" role="img" aria-label="Grabanlage aus hellem Granit" style="background:linear-gradient(#b3b8b4,#75786f)"></div><p>Lorem ipsum is simply dummy text of the printing and typesetting industry. Lorem</p></div>
<div class="abs thumb" style="left:875px"><div class="photo" role="img" aria-label="Grabstein mit Baummotiv" style="background:linear-gradient(#8f8e8c,#4a4846)"></div><p>Lorem ipsum is simply dummy text of the printing and typesetting industry. Lorem</p></div>

<!-- services -->
<h2 class="abs serif sec-title" style="left:0;top:862px;width:1200px">HELPING FAMILIES CONNECT,<br>HONOR &amp; REMEMBER</h2>
<p class="abs sec-lead">Lorem Ipsum is simply dummy text of the printing and typesetting industry.Lorem Ipsum is simply dummy text of the printing and typesetting industry.Lorem Ipsum</p>
<div class="abs book"></div>
<div class="abs svc" style="left:167px;top:1090px">
  <div class="photo" role="img" aria-label="Bestatter neben einem Grabstein" style="background:linear-gradient(#8ea27a,#3d3f38)"></div>
  <h3>FUNERAL<br>PROCESS</h3>
  <p>Lorem Ipsum is simply dummy text of the printing and typesetting industry. Lorem Ipsum has been the industry's</p>
</div>
<div class="abs svc" style="left:473px;top:1090px">
  <div class="photo" role="img" aria-label="Grabsteine mit Blumen" style="background:linear-gradient(#8c6a55,#4d3b30)"></div>
  <h3>TOMBSTONES<br>PROCESS</h3>
  <p>Lorem Ipsum is simply dummy text of the printing and typesetting industry. Lorem Ipsum has been the industry's</p>
</div>
<div class="abs svc" style="left:780px;top:1090px">
  <div class="photo" role="img" aria-label="Gepflegtes Grab mit Blumen" style="background:linear-gradient(#9a9c92,#4f5a3e)"></div>
  <h3>GRAVE<br>MAINTENANCE</h3>
  <p>Lorem Ipsum is simply dummy text of the printing and typesetting industry. Lorem Ipsum has been the industry's</p>
</div>
<div class="btn-outline btn-dark" style="left:200px;top:1490px;width:186px;height:48px">Read More</div>
<div class="btn-outline btn-dark" style="left:508px;top:1490px;width:186px;height:48px">Read More</div>
<div class="btn-outline btn-dark" style="left:816px;top:1490px;width:186px;height:48px">Read More</div>

<!-- banner -->
<div class="abs banner" role="img" aria-label="Friedhof mit Grabsteinen, abgedunkelt">
  <h2>A UNIQUE DIGITAL SPACE TO HONOR THOSE IMPORTANT<br>IN OUR LIVES IN A WAY AUTHENTIC TO THEM.</h2>
</div>
<div class="btn-outline btn-light" style="left:507px;top:1808px;width:186px;height:48px">Read More</div>

<!-- about -->
<div class="abs about-bg"></div>
<div class="abs" style="left:0;top:2075px;width:68px;height:300px;background:var(--dark)"></div>
<div class="abs" style="left:595px;top:1980px;width:445px;height:395px;background:var(--dark)"></div>
<div class="photo" role="img" aria-label="Mann im schwarzen Hemd an einer Landstraße" style="left:638px;top:1918px;width:360px;height:407px;background:linear-gradient(#8da36b,#4c5a3a 55%,#3a3c36)"></div>
<h2 class="abs serif about-title">LOREM IPSUM<br>LOREM IPSUM IS SIMPLY</h2>
<p class="abs about-text">Lorem Ipsum is simply dummy text of the printing and typesetting industry. Lorem Ipsum has been the industry's standard dummy text ever since the 1500s, when an unknown printer took a galley of type and scrambled it to make a type specimen</p>
<div class="btn-outline" style="left:110px;top:2257px;width:187px;height:48px">Read More</div>

<!-- gallery -->
<div class="abs" style="left:0;top:2375px;width:358px;height:630px;background:var(--dark)"></div>
<div class="abs" style="left:68px;top:2493px;width:270px;height:407px;border:5px solid #fff;padding:70px 28px 0 28px;color:#fff">
  <h4 class="serif" style="font-size:22px;color:var(--gold);font-weight:600">LOREM IPSUM IS</h4>
  <p style="font-size:12.5px;line-height:21px;margin-top:24px">Lorem Ipsum is dummy text of the printing and typesetting industry. Lorem Ipsum is simply dummy text of the printing and typesetting industry. Lorem Ipsum has been the industry's standard dummy</p>
</div>
<div class="photo" role="img" aria-label="Dunkler Grabstein mit Kuppel" style="left:358px;top:2375px;width:236px;height:255px;background:linear-gradient(#6a6760,#2e2d2a)"></div>
<div class="abs cell-text" style="left:594px;top:2375px;width:160px;height:255px;background:#fff;padding:42px 14px 0 16px"><h4>LOREM<br>IPSUM IS</h4><p>Lorem Ipsum is dummy text of the printing and typesetting industry.</p></div>
<div class="photo" role="img" aria-label="Grabstein mit Engelsfigur" style="left:754px;top:2375px;width:446px;height:223px;background:linear-gradient(#9ea0a3,#5d5f62)"></div>
<div class="abs cell-text" style="left:358px;top:2630px;width:236px;height:200px;background:#fff;padding:50px 14px 0 18px"><h4>LOREM IPSUM IS</h4><p>Lorem Ipsum is dummy text of the printing and typesetting industry.</p></div>
<div class="photo" role="img" aria-label="Rötlicher Grabstein mit Blumen" style="left:594px;top:2630px;width:160px;height:268px;background:linear-gradient(#8a5a6a,#5b3a42)"></div>
<div class="abs cell-text" style="left:754px;top:2598px;width:164px;height:232px;background:#fff;padding:58px 12px 0 20px"><h4>LOREM<br>IPSUM IS</h4><p>Lorem Ipsum is dummy text of the printing and typesetting industry.</p></div>
<div class="photo" role="img" aria-label="Grabstein mit Relief einer Frau" style="left:918px;top:2598px;width:282px;height:407px;background:linear-gradient(#c9c8c6,#8c8b89)"></div>
<div class="photo" role="img" aria-label="Grabstein aus dunklem Granit" style="left:358px;top:2830px;width:236px;height:175px;background:linear-gradient(#7b7f83,#3f4245)"></div>
<div class="photo" role="img" aria-label="Grabstein vor einem Haus" style="left:754px;top:2830px;width:164px;height:175px;background:linear-gradient(#8a8d90,#45484a)"></div>
<div class="abs" style="left:483px;top:2963px;width:304px;height:47px;background:var(--gold);color:#fff;font-size:19px;display:flex;align-items:center;justify-content:center">Click Here Download PDF</div>

<!-- testimonial -->
<h2 class="abs serif" style="left:500px;top:3060px;font-size:28px;line-height:37px;color:var(--gold);font-weight:600">WHAT OUR<br>FAMILIES SAY</h2>
<div class="photo" role="img" aria-label="Porträtfoto einer Kundin" style="left:255px;top:3173px;width:184px;height:184px;border-radius:50%;background:radial-gradient(#a98b74,#5a4436)"></div>
<p class="abs quote">Lorem Ipsum is simply dummy text of the printing and typesetting industry. Lorem Ipsum has been the industry's standard dummy text ever since the 1500s,</p>
<div class="abs dots"><span></span><span></span><span></span><span></span></div>

<!-- contact -->
<div class="abs" style="left:0;top:3480px;width:613px;height:602px;background:#fff"></div>
<div class="photo" role="img" aria-label="Grab mit roten Blumen auf einem Friedhof" style="left:613px;top:3480px;width:587px;height:602px;background:linear-gradient(135deg,#5c5a55,#3a3833 60%,#2e2c29)"></div>
<div class="abs contact-card">
  <div><svg width="16" height="18" viewBox="0 0 16 18"><path d="M8 0a6 6 0 016 6c0 4.5-6 12-6 12S2 10.5 2 6a6 6 0 016-6zm0 4a2 2 0 100 4 2 2 0 000-4z" fill="#333"/></svg><span>lindenweg 12<br>30159 hannover</span></div>
  <div><svg width="16" height="16" viewBox="0 0 24 24"><path d="M6.6 10.8a15 15 0 006.6 6.6l2.2-2.2a1 1 0 011-.25 11 11 0 003.6.6 1 1 0 011 1V20a1 1 0 01-1 1A17 17 0 013 4a1 1 0 011-1h3.5a1 1 0 011 1 11 11 0 00.6 3.6 1 1 0 01-.25 1z" fill="#333"/></svg><span>0151-2030-4455</span></div>
  <div><svg width="18" height="14" viewBox="0 0 18 14"><rect x="1" y="1" width="16" height="12" fill="none" stroke="#333" stroke-width="2"/><path d="M1 1l8 7 8-7" stroke="#333" stroke-width="2" fill="none"/></svg><span>info@nur-samira.eu</span></div>
  <div><svg width="18" height="18" viewBox="0 0 18 18"><circle cx="9" cy="9" r="8" fill="none" stroke="#333" stroke-width="1.6"/><path d="M1 9h16M9 1c-4 4-4 12 0 16M9 1c4 4 4 12 0 16" stroke="#333" stroke-width="1.4" fill="none"/></svg><span>www.nur-samira.eu</span></div>
</div>
<div class="abs" style="left:345px;top:3555px;width:260px;height:440px;background:#fff;box-shadow:0 0 10px rgba(0,0,0,.15);padding:10px">
  <div role="img" aria-label="Stadtplan mit Standort" style="width:100%;height:100%;background:linear-gradient(135deg,#e8ece4,#dfe6d9)"></div>
</div>
<div class="abs form">
  <h3>SEND US YOUR MESSAGES!</h3>
  <div class="box">
    <label>NAME</label><div class="field"></div>
    <label>EMAIL</label><div class="field"></div>
    <label>PHONE</label><div class="field"></div>
    <label>MESSAGE</label><div class="field" style="height:58px"></div>
    <div class="send">SEND YOUR MESSAGE</div>
  </div>
</div>

<!-- footer -->
<footer class="abs footer">
  <div class="abs" style="left:132px;top:120px;font-family:'Cinzel',serif;font-weight:700;font-size:32px;color:#fff;display:flex;align-items:center;gap:12px"><i style="width:24px;height:24px;border:2px solid #fff;border-radius:50%;display:block"></i>NUR-SAMIRA</div>
  <h5 style="left:400px">QUICK LINKS</h5>
  <ul style="left:400px;top:85px"><li>Privacy Policy</li><li>Condition of Use</li><li>Notice Policy</li><li>Website Policy</li></ul>
  <h5 style="left:617px">HOURS</h5>
  <ul style="left:600px;top:85px"><li>Monday–Friday:</li><li>8:30AM–8:30PM</li></ul>
  <h5 style="left:820px">CONTACT INFORMATION</h5>
  <ul style="left:822px;top:85px;line-height:16px">
    <li style="margin-bottom:18px">◉&nbsp; lindenweg 12<br>&nbsp;&nbsp;&nbsp;&nbsp;&nbsp;30159 hannover</li>
    <li style="margin-bottom:18px">✆&nbsp; 0151-2030-4455</li>
    <li style="margin-bottom:18px">✉&nbsp; info@nur-samira.eu</li>
    <li>◎&nbsp; www.nur-samira.eu</li>
  </ul>
  <div class="abs" style="left:170px;top:248px;width:860px;height:1px;background:#777"></div>
  <div class="abs" style="left:170px;top:290px;font-size:11px;color:#fff">©2021 nur-samira.eu All Rights reserved.</div>
  <div class="abs social" style="left:898px;top:280px"><span></span><span></span><span></span></div>
</footer>

</body>
</html>
```